A wine Label for a new brand of New Zealand Wine

We are looking for a Wine Label for our "Harbor Crest" brand of wines from North Otago New Zealand. We would like the label to perhaps use the HC as a logo and the rest up to the designer. We have our vineyards located in the Waitaki Valley New Zealand which is a southern region with mountains and a river flowing past our vineyard. Photos attached of Dramatic Landscape. Also attached is a basic outline of requirements for the front bottle of the label. The rear bottle label will contain writing about the wines background plus statutory regulations on Alc. Vol, bar code etc. Front Label size to be no Larger than 80mm deep by 100 mm wide. The label can be simple or graphic, whatever the designer chooses.
Target Market(s)
New Wine Brand
Look and feel
Each slider illustrates characteristics of the customer's brand and the style your logo design should communicate.

```html
<!DOCTYPE html>
<html lang="en">
<head>
<meta charset="utf-8">
<title>Harbor Crest – Pinot Gris 2015 Label Options</title>
<link rel="stylesheet" href="https://fonts.googleapis.com/css2?family=League+Spartan:wght@800&family=Jost:wght@500;600&display=swap">
<style>
  :root {
    --backdrop: #333333;
    --tan: #d1a45f;
    --brown: #8a4a1b;
    --title-outline: #7a3e14;
    --gold-line: #f2c21b;
    --pale-gold: #fff4c4;
    --cream-text: #f8e18e;
    --white: #ffffff;
    --photo-light: #b59a6e;
    --photo-dark: #6a5a34;
  }
  * { margin: 0; padding: 0; box-sizing: border-box; }
  html, body {
    width: 1200px; height: 750px; overflow: hidden;
    background: var(--backdrop);
  }
  .canvas { position: relative; width: 1200px; height: 750px; }

  .label {
    position: absolute; top: 80px; width: 472px; height: 590px;
    background: var(--tan);
  }
  .label--split { left: 88px; }
  .label--solid { left: 640px; }

  .label__frame {
    position: absolute; left: 22px; top: 22px; width: 428px; height: 546px;
    overflow: hidden;
  }
  .label--split .label__frame {
    border: 2px solid var(--gold-line);
    background: linear-gradient(var(--tan) 0 268px, var(--brown) 268px);
  }
  .label--solid .label__frame {
    border: 2px solid transparent;
    background:
      linear-gradient(var(--brown), var(--brown)) padding-box,
      linear-gradient(135deg, var(--gold-line), var(--pale-gold) 30%, var(--gold-line) 55%, var(--pale-gold) 80%, var(--gold-line)) border-box;
  }

  .monogram {
    position: absolute; left: 50%; top: 18px; transform: translateX(-50%);
    font-family: "League Spartan", sans-serif; font-weight: 800;
    font-size: 34px; line-height: 47px; letter-spacing: -1px;
  }
  .label--split .monogram { color: var(--brown); }
  .label--solid .monogram { color: var(--tan); }

  .wine-title {
    position: absolute; left: 0; width: 100%; text-align: center;
    font-family: "League Spartan", sans-serif; font-weight: 800;
    line-height: 1; text-transform: uppercase;
  }
  .label--split .wine-title {
    top: 80px; font-size: 60px; color: var(--white);
    -webkit-text-stroke: 6px var(--title-outline); paint-order: stroke fill;
  }
  .label--split .wine-title span { display: block; height: 55px; }
  .label--solid .wine-title {
    top: 90px; font-size: 58px; color: var(--tan);
  }
  .label--solid .wine-title span { display: block; height: 58px; }

  .varietal {
    position: absolute; left: 0; width: 100%; text-align: center;
    font-family: "Jost", sans-serif; font-weight: 600;
    font-size: 24px; line-height: 30px; letter-spacing: 0.5px;
  }
  .label--split .varietal { top: 195px; color: var(--brown); }
  .label--solid .varietal { top: 216px; color: var(--tan); }

  .landscape {
    position: absolute; left: 109px; top: 297px; width: 206px; height: 168px;
    background: linear-gradient(160deg, var(--photo-light), var(--photo-dark));
  }

  .origin {
    position: absolute; left: 0; width: 100%; text-align: center;
    font-family: "Jost", sans-serif; color: var(--cream-text);
  }
  .origin--region { top: 478px; font-size: 14px; font-weight: 500; }
  .origin--country { top: 502px; font-size: 11.5px; font-weight: 600; }
</style>
</head>
<body>
<main class="canvas">

  <section class="label label--split">
    <div class="label__frame">
      <div class="monogram">HC</div>
      <h1 class="wine-title"><span>Harbor</span><span>Crest</span></h1>
      <p class="varietal">PINOT GRIS<br>2015</p>
      <div class="landscape" role="img" aria-label="Landscape photograph of the vineyard valley with mountains and a river"></div>
      <p class="origin origin--region">Waitaki Valley - North Otago</p>
      <p class="origin origin--country">New Zealand Wine</p>
    </div>
  </section>

  <section class="label label--solid">
    <div class="label__frame">
      <div class="monogram">HC</div>
      <h2 class="wine-title"><span>Harbor</span><span>Crest</span></h2>
      <p class="varietal">PINOT GRIS<br>2015</p>
      <div class="landscape" role="img" aria-label="Landscape photograph of the vineyard valley with mountains and a river"></div>
      <p class="origin origin--region">Waitaki Valley - North Otago</p>
      <p class="origin origin--country">New Zealand Wine</p>
    </div>
  </section>

</main>
</body>
</html>
```